Finch Haulage Ltd

We need an A5 size (UK size) flyer to advertise our new business which is called Finch Haulage.
Domestic and Commercial Waste Clearance Services.
Please have the question in bold "Do you have a pile of junk you need to dispose of?"
We collect all kinds of junk or rubbish from homes and businesses across Kent, Sussex and South London.
No fuss, no mess!
A low cost, hassle free alternative to skip hire.
Licensed by the Landcare Board and fully insured (this can be in small print at the bottom).
Please put the Recycle symbol somewhere.
Our tagline on our vehicle is "We Clear More, For Less!"
We'd like the flyer to be bold and eye-catching (to catch the eye of the homeowner or business owner while it's sitting on their doormat).
We need our telephone, website and email to be prominent. Maybe saying "Call today for a free quote"
Tel. 01734 586019
Email: info@finchhaulage.example.co.uk
www.finchhaulage.example.co.uk
Target Market(s)
Our market will be homes and small businesses around Kent, Sussex and South London.

```html
<!DOCTYPE html>
<html lang="en">
<head>
<meta charset="utf-8">
<title>Finch Haulage – A5 Flyer</title>
<link rel="stylesheet" href="https://fonts.googleapis.com/css2?family=Open+Sans:wght@600;700;800&family=Stardos+Stencil:wght@700&display=swap">
<style>
  :root {
    --board-grey: #bdbdbd;
    --frame-black: #000000;
    --header-blue: #00a8e8;
    --flyer-orange: #f7941d;
    --headline-white: #ffffff;
    --tagline-ink: #0d0d0d;
    --brand-grey: #5b5b5b;
    --label-ink: #111111;
    --recycle-green: #2e8b3a;
    --photo-dark: #4a3a2e;
    --photo-mid: #8c7a66;
    --photo-light: #c9c2b6;
  }
  * { margin: 0; padding: 0; box-sizing: border-box; }
  html, body {
    width: 1200px; height: 1000px; overflow: hidden;
    background: var(--board-grey);
  }
  .board { position: relative; width: 1200px; height: 1000px; }

  .flyer {
    position: absolute; left: 47px; top: 80px;
    width: 612px; height: 876px;
    border: 4px solid var(--frame-black);
    background: var(--flyer-orange);
    overflow: hidden;
    font-family: "Open Sans", Arial, sans-serif;
  }
  .flyer__header {
    position: absolute; left: 0; top: 0; width: 100%; height: 187px;
    background: var(--header-blue);
  }
  .headline {
    position: absolute;
    color: var(--headline-white);
    font-weight: 700;
    font-variant: small-caps;
    text-shadow: 2px 2px 0 #1a1a1a;
    white-space: nowrap;
  }
  .headline--first { top: 10px; left: 24px; font-size: 49px; }
  .headline--second { top: 82px; left: 64px; font-size: 45px; }
  .tagline {
    position: absolute; top: 146px; left: 86px;
    color: var(--tagline-ink);
    font-weight: 700; font-size: 28px;
    font-variant: small-caps; letter-spacing: 4.5px;
    white-space: nowrap;
  }

  .flyer__photo {
    position: absolute; left: 56px; top: 187px;
    width: 556px; height: 544px;
  }

  .services {
    position: absolute; left: 0; width: 100%; text-align: center;
    white-space: nowrap;
  }
  .services--main {
    top: 733px; font-size: 15px; font-weight: 700;
    color: var(--headline-white); text-shadow: 1px 1px 0 #2a2a2a;
  }
  .services--promise {
    top: 755px; font-size: 13.5px; font-weight: 700;
    color: var(--tagline-ink);
  }

  .brand {
    position: absolute; left: 18px; top: 790px;
    display: flex; align-items: center; gap: 10px;
    font-weight: 800; font-size: 30px;
    color: var(--brand-grey);
    white-space: nowrap;
  }
  .brand__mark { width: 18px; height: 18px; background: var(--brand-grey); }

  .small-print {
    position: absolute; left: 18px; top: 836px;
    display: flex; align-items: center; gap: 8px;
    font-size: 10.5px; font-weight: 600; line-height: 13px;
    color: var(--tagline-ink);
  }
  .small-print__icon { width: 26px; height: 26px; flex: none; }

  .contact {
    position: absolute; right: 12px; top: 782px;
    list-style: none; text-align: right;
    font-weight: 600; font-size: 17px; line-height: 21px;
    color: var(--headline-white);
    text-shadow: 1px 1px 0 #2a2a2a;
    white-space: nowrap;
  }
  .contact__call {
    color: var(--tagline-ink); text-shadow: none; font-weight: 800;
  }

  .spec-label {
    position: absolute; left: 700px; top: 170px; width: 450px;
    text-align: center;
    font-family: "Stardos Stencil", Impact, sans-serif;
    font-weight: 700; font-size: 58px; line-height: 64px;
    color: var(--label-ink);
  }
</style>
</head>
<body>
<main class="board">
  <section class="flyer">
    <header class="flyer__header">
      <h1 class="headline headline--first">Do you have a pile of junk</h1>
      <p class="headline headline--second">you need to dispose of?</p>
      <p class="tagline">We Clear More, For Less!</p>
    </header>

    <svg class="flyer__photo" width="556" height="544" viewBox="0 0 556 544" role="img" aria-label="Photograph of a garden pile of junk: broken boards, timber offcuts, carpet and rubbish bags in front of a wooden fence">
      <defs>
        <linearGradient id="junk-tones" x1="0" y1="0" x2="0" y2="1">
          <stop offset="0" stop-color="var(--photo-dark)"/>
          <stop offset="0.45" stop-color="var(--photo-mid)"/>
          <stop offset="0.8" stop-color="var(--photo-light)"/>
          <stop offset="1" stop-color="#6d6a66"/>
        </linearGradient>
      </defs>
      <circle cx="275" cy="272" r="272" fill="url(#junk-tones)" stroke="#222" stroke-width="1.5"/>
    </svg>

    <p class="services services--main">Domestic &amp; Commercial Waste Clearance – Kent, Sussex &amp; South London</p>
    <p class="services services--promise">No fuss, no mess! A low cost, hassle free alternative to skip hire.</p>

    <div class="brand">
      <span class="brand__mark"></span>
      <span class="brand__name">Finch Haulage</span>
    </div>

    <div class="small-print">
      <svg class="small-print__icon" viewBox="0 0 26 26" role="img" aria-label="Recycle symbol">
        <g fill="none" stroke="var(--recycle-green)" stroke-width="2.4" stroke-linecap="round" stroke-linejoin="round">
          <path d="M9 8 L13 2 L17 8"/>
          <path d="M15 5 L11 5"/>
          <path d="M20 11 L24 18 L20 23"/>
          <path d="M22 21 L17 23"/>
          <path d="M13 23 L3 23 L6 15"/>
          <path d="M3 17 L6 15 L8 18"/>
        </g>
      </svg>
      <p>Licensed by the Landcare Board.<br>Fully insured. We recycle wherever possible.</p>
    </div>

    <ul class="contact">
      <li class="contact__call">Call today for a free quote</li>
      <li>01734 586019</li>
      <li>info@finchhaulage.example.co.uk</li>
      <li>www.finchhaulage.example.co.uk</li>
    </ul>
  </section>

  <p class="spec-label">FLYER DESIGN<br>SIZE = A5</p>
</main>
</body>
</html>
```